Business Card Design

We sell fish products to corporate food companies who then turn these products into final food products for consumers

Industry/Entity Type

Business

Contact Information for Business Card

I need a corporate business card template for a fish products business. We would like it be professional for use in dealing with multi national companies. This company business card template will be used by multiple employees so the following fields must be open to edit (Name, Phone Number and Email address)

```html
<!DOCTYPE html>
<html lang="en">
<head>
<meta charset="utf-8">
<title>Tidewell Seafoods – Business Card</title>
<link rel="stylesheet" href="https://fonts.googleapis.com/css2?family=Open+Sans:wght@400;600;700&display=swap">
<style>
  :root {
    --backdrop: #e9eaec;
    --card-white: #ffffff;
    --brand-blue: #0b5cad;
    --brand-navy: #1d4f99;
    --accent-cyan: #22b4e3;
    --accent-green: #66c67a;
    --text-light: #ffffff;
  }
  * { margin: 0; padding: 0; box-sizing: border-box; }
  html, body {
    width: 1200px;
    height: 800px;
    overflow: hidden;
    background: var(--backdrop);
    font-family: "Open Sans", Arial, sans-serif;
  }
  .canvas {
    width: 1200px;
    height: 800px;
    display: flex;
    align-items: center;
    justify-content: center;
  }
  .business-card {
    width: 390px;
    height: 680px;
    background: var(--card-white);
    display: flex;
    flex-direction: column;
    box-shadow: 0 10px 30px rgba(0,0,0,0.15);
  }
  .card-top {
    height: 45%;
    display: flex;
    align-items: center;
    justify-content: center;
  }
  .brand {
    display: flex;
    align-items: center;
    gap: 12px;
  }
  .brand-mark {
    width: 22px;
    height: 22px;
    border-radius: 50%;
    background: var(--accent-cyan);
  }
  .brand-name {
    font-weight: 700;
    font-size: 28px;
    color: var(--brand-navy);
    letter-spacing: 0.5px;
  }
  .accent-stripe {
    height: 8px;
    background: var(--accent-cyan);
  }
  .card-bottom {
    flex: 1;
    background: var(--brand-blue);
    color: var(--text-light);
    padding: 46px 36px 0 150px;
  }
  .person-name {
    font-size: 27px;
    font-weight: 700;
    line-height: 1.1;
  }
  .person-name .surname { color: var(--accent-green); }
  .person-title {
    font-size: 15px;
    margin-top: 4px;
    margin-bottom: 30px;
  }
  .contact-list { list-style: none; }
  .contact-item {
    display: flex;
    align-items: center;
    gap: 12px;
    font-size: 15px;
    margin-bottom: 12px;
  }
  .contact-icon {
    width: 16px;
    height: 16px;
    flex: none;
  }
</style>
</head>
<body>
<main class="canvas">
  <article class="business-card">
    <header class="card-top">
      <div class="brand">
        <span class="brand-mark"></span>
        <span class="brand-name">Tidewell Seafoods</span>
      </div>
    </header>
    <div class="accent-stripe"></div>
    <section class="card-bottom">
      <h1 class="person-name">Marten <span class="surname">Ekdal</span></h1>
      <p class="person-title">Director</p>
      <ul class="contact-list">
        <li class="contact-item">
          <svg class="contact-icon" viewBox="0 0 16 16" fill="#fff"><path d="M3 1h3l1.5 4-2 1.2a9 9 0 0 0 4.3 4.3L11 8.5l4 1.5v3a2 2 0 0 1-2 2A12 12 0 0 1 1 3a2 2 0 0 1 2-2z"/></svg>
          <span>(555) 0142-0011</span>
        </li>
        <li class="contact-item">
          <svg class="contact-icon" viewBox="0 0 16 16" fill="none" stroke="#fff" stroke-width="1.6"><rect x="4" y="1" width="8" height="14" rx="1.5"/><line x1="7" y1="12.5" x2="9" y2="12.5"/></svg>
          <span>(555)-0198-0125</span>
        </li>
        <li class="contact-item">
          <svg class="contact-icon" viewBox="0 0 16 16" fill="none" stroke="#fff" stroke-width="1.6"><rect x="1" y="3" width="14" height="10" rx="1"/><path d="M1.5 3.5 8 9l6.5-5.5"/></svg>
          <span>marten@tidewell.com</span>
        </li>
        <li class="contact-item">
          <svg class="contact-icon" viewBox="0 0 16 16" fill="none" stroke="#fff" stroke-width="1.4"><circle cx="8" cy="8" r="6.5"/><ellipse cx="8" cy="8" rx="3" ry="6.5"/><line x1="1.5" y1="8" x2="14.5" y2="8"/></svg>
          <span>www.tidewell.com</span>
        </li>
      </ul>
    </section>
  </article>
</main>
</body>
</html>
```